New Brimolux Poster

This is for designer Marlowe ONLY.<br/><br/>hi marlowe,<br/><br/>Hope you are well.<br/>I need to redo my Brimolux combo. <br/>So the layout I want is clean and simple. <br/>Photo is on the left hand side, then combo's details and price.<br/>Same poster size.<br/>Thank you<br/><br/><br/>Pho Combo: 1x Pho + 1x Side + 1x Drinks = $23<br/>Noodle Salad Combo: 1x Noodle Salads + 1x Side + 1x Drinks = $23<br/>Rice Combo: 1x Rice + 1x Side + 1x Drinks = $25<br/>Combo for 2: 2x mains + 1x side + 2x Drinks = $39<br/>Family Combo: 4x mains + 2 sides + 4x Drinks = 79

```html
<!DOCTYPE html>
<html lang="en">
<head>
<meta charset="utf-8">
<title>Brimolux Combos Poster</title>
<link rel="stylesheet" href="https://fonts.googleapis.com/css2?family=Kalam:wght@700&family=Open+Sans:wght@600;800&display=swap">
<style>
  :root {
    --stage: #5f7476;
    --board: #2c2c2c;
    --board-deep: #232323;
    --photo-well: #1c1c1c;
    --accent: #e07b1a;
    --ink: #f4f1ec;
  }
  * { box-sizing: border-box; margin: 0; padding: 0; }
  html, body { width: 1200px; height: 1200px; overflow: hidden; }
  body { background: var(--stage); font-family: "Open Sans", sans-serif; color: var(--ink); }

  .poster {
    position: absolute; left: 175px; top: 0;
    width: 849px; height: 1200px;
    background: radial-gradient(ellipse at 40% 30%, var(--board) 0%, var(--board-deep) 100%);
  }

  .poster-title {
    position: absolute; left: 65px; top: 70px; width: 460px;
    font-family: "Kalam", cursive; font-weight: 700; text-align: center;
    line-height: 1; letter-spacing: 2px;
  }
  .poster-title .main { display: block; font-size: 72px; }
  .poster-title .sub { display: block; font-size: 50px; margin-top: 4px; margin-left: 10px; }

  .brand-mark {
    position: absolute; left: 645px; top: 120px;
    display: flex; align-items: center; gap: 8px;
    font-weight: 800; font-size: 18px; color: var(--accent); letter-spacing: 1px;
  }
  .brand-mark .dot {
    width: 16px; height: 16px; border: 2px solid var(--accent); border-radius: 50%;
  }

  .combo-list { position: absolute; left: 65px; top: 216px; width: 719px; }
  .combo {
    position: relative; height: 169px; margin-bottom: 17px;
    border: 2px solid var(--accent);
    display: flex;
  }
  .combo-photo {
    width: 288px; height: 100%;
    background: radial-gradient(ellipse at 50% 55%, #5a5448 0%, #2d2b27 45%, var(--photo-well) 80%);
  }
  .combo-info { flex: 1; padding-left: 12px; display: flex; flex-direction: column; justify-content: center; }
  .combo-name { font-weight: 800; font-size: 26px; line-height: 1.1; letter-spacing: 0.3px; }
  .combo-parts { font-weight: 600; font-size: 14.5px; margin-top: 2px; letter-spacing: 0.3px; }
  .combo-parts b { font-weight: 800; }
  .combo-price {
    position: absolute; right: 10px; top: 50%; transform: translateY(-50%);
    font-weight: 800; font-size: 32px;
  }
</style>
</head>
<body>
<div class="poster">
  <h1 class="poster-title">
    <span class="main">BRIMOLUX</span>
    <span class="sub">COMBOS</span>
  </h1>

  <div class="brand-mark"><span class="dot"></span>Bowl &amp; Dash</div>

  <div class="combo-list">
    <section class="combo">
      <div class="combo-photo" role="img" aria-label="Phở bowl with a plate of side dish and a bottled iced tea"></div>
      <div class="combo-info">
        <h2 class="combo-name">PHỞ COMBO</h2>
        <p class="combo-parts"><b>1x</b> PHỞ + <b>1x</b> SIDE + <b>1x</b> DRINKS</p>
      </div>
      <div class="combo-price">$23</div>
    </section>

    <section class="combo">
      <div class="combo-photo" role="img" aria-label="Noodle salad bowl with rice paper rolls, dipping sauce and a bottled drink"></div>
      <div class="combo-info">
        <h2 class="combo-name">NOODLE SALAD COMBO</h2>
        <p class="combo-parts"><b>1x</b> NOODLE SALAD + <b>1x</b> SIDE + <b>1x</b> DRINKS</p>
      </div>
      <div class="combo-price">$23</div>
    </section>

    <section class="combo">
      <div class="combo-photo" role="img" aria-label="Rice plate with stir-fry, spring rolls with dipping sauce and a bottled drink"></div>
      <div class="combo-info">
        <h2 class="combo-name">RICE COMBO</h2>
        <p class="combo-parts"><b>1x</b> RICE + <b>1x</b> SIDE + <b>1x</b> DRINKS</p>
      </div>
      <div class="combo-price">$25</div>
    </section>

    <section class="combo">
      <div class="combo-photo" role="img" aria-label="Two main dishes, spring rolls and two bottled drinks"></div>
      <div class="combo-info">
        <h2 class="combo-name">COMBO FOR 2</h2>
        <p class="combo-parts"><b>2x</b> MAINS + <b>1x</b> SIDE + <b>2x</b> DRINKS</p>
      </div>
      <div class="combo-price">$39</div>
    </section>

    <section class="combo">
      <div class="combo-photo" role="img" aria-label="Four main dishes, two side plates and four bottled drinks"></div>
      <div class="combo-info">
        <h2 class="combo-name">FAMILY COMBO</h2>
        <p class="combo-parts"><b>4x</b> MAINS + <b>2x</b> SIDES + <b>4x</b> DRINKS</p>
      </div>
      <div class="combo-price">$79</div>
    </section>
  </div>
</div>
</body>
</html>
```